Business Card Design Project

Combined with our Logo design project we are also after a template business card for our business "Veltrix"

We are a business to business firm that provides professional turnkey aerial (Drone) asset inspection solutions (Video/Photo/Survey/Thermal) for customers like Electrical, Water and Gas utilities, Energy generation companies and such.

The final design should be communicate safety (first and foremost), clean, reliabie and trust worthy

Target Market(s)

Business to business, particularly conservative large business owners whom are risk adverse.

Industry/Entity Type

Safety

Requirements
Must have
• Clean and fresh

```html
<!DOCTYPE html>
<html lang="en">
<head>
<meta charset="utf-8">
<title>Veltrix Business Card</title>
<link rel="stylesheet" href="https://fonts.googleapis.com/css2?family=Montserrat:wght@300;400;500;600&display=swap">
<style>
  :root {
    --navy: #1d3f6e;
    --navy-deep: #15315a;
    --navy-light: #28558c;
    --white: #ffffff;
    --ink: #1a1a1a;
    --grey: #8a8a8a;
    --backdrop: #2b2b2b;
    --font: "Montserrat", sans-serif;
  }
  * { box-sizing: border-box; margin: 0; padding: 0; }
  html, body {
    width: 1200px; height: 1000px; overflow: hidden;
    background: var(--backdrop);
    font-family: var(--font);
  }
  .sheet {
    width: 1200px; height: 1000px;
    display: flex; flex-direction: column; align-items: center; justify-content: center;
    gap: 52px;
  }
  .card {
    position: relative;
    width: 760px; height: 434px;
    overflow: hidden;
    box-shadow: 0 10px 30px rgba(0,0,0,.45);
  }
  .card__art { position: absolute; inset: 0; width: 100%; height: 100%; }

  /* Front */
  .card--front { background: var(--white); }
  .brand {
    position: absolute; left: 110px; top: 108px;
    display: flex; align-items: center; gap: 12px;
  }
  .brand__dot {
    width: 44px; height: 44px; border-radius: 50%;
    background: var(--navy);
  }
  .brand__name {
    font-weight: 600; font-size: 22px; letter-spacing: 2px;
    color: var(--navy);
  }
  .person { position: absolute; left: 300px; top: 92px; }
  .person__name {
    font-weight: 300; font-size: 36px; letter-spacing: 2px;
    color: var(--ink);
  }
  .person__role {
    margin-top: 6px;
    font-weight: 400; font-size: 19px; letter-spacing: 2px;
    color: var(--grey);
  }
  .address {
    position: absolute; left: 62px; top: 300px;
    list-style: none;
    color: var(--white); font-size: 17px; line-height: 34px;
  }
  .contacts {
    position: absolute; left: 440px; top: 248px;
    list-style: none;
    color: var(--white); font-size: 17px;
  }
  .contacts__item {
    display: flex; align-items: center; gap: 20px;
    height: 36px;
  }
  .contacts__icon { width: 22px; height: 22px; flex: none; }

  /* Back */
  .card--back {
    background: linear-gradient(150deg, var(--navy-light) 0%, var(--navy) 55%, var(--navy-deep) 100%);
  }
  .back-brand {
    position: absolute; right: 70px; top: 150px;
    text-align: left;
  }
  .back-brand__name {
    font-weight: 600; font-size: 50px; letter-spacing: 3px;
    color: var(--white);
  }
  .back-brand__web {
    margin-top: 8px;
    font-weight: 400; font-size: 15px; letter-spacing: 1px;
    color: var(--white);
  }
</style>
</head>
<body>
<main class="sheet">

  <section class="card card--front" aria-label="Business card front">
    <svg class="card__art" viewBox="0 0 760 434" preserveAspectRatio="none" aria-hidden="true">
      <defs>
        <linearGradient id="bandFill" x1="0" y1="0" x2="1" y2="1">
          <stop offset="0" stop-color="#1f4577"/>
          <stop offset="1" stop-color="#18365f"/>
        </linearGradient>
      </defs>
      <path d="M0 268 Q 330 178 760 150 L760 434 L0 434 Z" fill="url(#bandFill)"/>
      <path d="M0 262 Q 60 255 110 300 Q 60 275 0 290 Z" fill="#ffffff"/>
      <path d="M250 405 Q 520 420 760 350 L760 362 Q 520 432 250 405 Z" fill="#ffffff"/>
    </svg>

    <div class="brand">
      <span class="brand__dot"></span>
      <span class="brand__name">VELTRIX</span>
    </div>

    <div class="person">
      <h1 class="person__name">DANIEL HART</h1>
      <p class="person__role">PRESIDENT</p>
    </div>

    <ul class="address">
      <li>42 Harbour Rd</li>
      <li>Eastwood NSW 2199</li>
      <li>Australia</li>
    </ul>

    <ul class="contacts">
      <li class="contacts__item">
        <svg class="contacts__icon" viewBox="0 0 22 22" aria-hidden="true">
          <circle cx="11" cy="11" r="11" fill="#fff"/>
          <rect x="7.5" y="5" width="7" height="12" rx="1.3" fill="none" stroke="#1d3f6e" stroke-width="1.6"/>
          <circle cx="11" cy="14.8" r=".9" fill="#1d3f6e"/>
        </svg>
        <span>+61 (03) 5550 1927</span>
      </li>
      <li class="contacts__item">
        <svg class="contacts__icon" viewBox="0 0 22 22" aria-hidden="true">
          <circle cx="11" cy="11" r="11" fill="#fff"/>
          <path d="M7.2 5.5 L9.2 5.5 L10 8.6 L8.7 9.6 Q9.8 12.3 12.4 13.3 L13.4 12 L16.5 12.8 L16.5 14.8 Q16.3 16.5 14.6 16.5 Q6 15.6 5.5 7.4 Q5.6 5.6 7.2 5.5 Z" fill="#1d3f6e"/>
        </svg>
        <span>1800 555 019</span>
      </li>
      <li class="contacts__item">
        <svg class="contacts__icon" viewBox="0 0 22 22" aria-hidden="true">
          <circle cx="11" cy="11" r="11" fill="#fff"/>
          <rect x="5.5" y="7" width="11" height="8" fill="#1d3f6e"/>
          <path d="M5.5 7 L11 11.5 L16.5 7" fill="none" stroke="#fff" stroke-width="1.2"/>
        </svg>
        <span>danielhart@veltrix.com.au</span>
      </li>
    </ul>
  </section>

  <section class="card card--back" aria-label="Business card back">
    <div class="back-brand">
      <p class="back-brand__name">VELTRIX</p>
      <p class="back-brand__web">www.veltrix.com.au</p>
    </div>
  </section>

</main>
</body>
</html>
```